Label design for E-Liquid bottle
Velvet Pulse
Project: Label design for E-Liquid bottle
Label design for E-Liquid bottle - Manufacturing
Creative Brief
Need some graphic design for a label that will be used on a bottle of electronic cigarette E-Liquid. The name of the brand is Velvet Pulse. The theme will involve elements from the disco era.
Manufacturing
Will need some graphic design and project created with Photoshop. Winner will need to provide PSD file (editable layers) along with file of any font used. As flavors will change frequently, the file must be editable. The label should be fun and groovy. File format size should be 1800w x 900h Label will require certain text and criteria which I will provide.

```html
<!DOCTYPE html>
<html lang="en">
<head>
<meta charset="utf-8">
<title>Velvet Pulse E-Liquid Label</title>
<link rel="stylesheet" href="https://fonts.googleapis.com/css2?family=Shrikhand&family=Righteous&family=Lobster&family=Open+Sans:wght@400;600;700&display=swap">
<style>
  :root {
    --page-bg: #e4e4e6;
    --label-dark: #1a1020;
    --label-purple: #3b1f52;
    --swirl-magenta: #b0286a;
    --swirl-teal: #1f7a72;
    --swirl-orange: #d8741e;
    --ball-silver: #b9b3c2;
    --panel-bg: rgba(10, 8, 14, 0.86);
    --panel-edge: rgba(255, 255, 255, 0.18);
    --ingredient-green: #9bd13a;
    --warning-red: #ff3d2e;
    --title-gold: #f7b21c;
    --flavor-yellow: #f5d22a;
    --text-white: #ffffff;
    --batch-bg: #ffffff;
    --batch-text: #1a1a1a;
  }
  * { box-sizing: border-box; margin: 0; padding: 0; }
  html, body {
    width: 1200px; height: 600px; overflow: hidden;
    background: var(--page-bg);
  }
  .label {
    position: absolute; left: 30px; top: 15px;
    width: 1140px; height: 570px;
    overflow: hidden;
    background: var(--label-dark);
  }
  .label__art {
    position: absolute; inset: 0;
    background:
      radial-gradient(circle at 50% 100%, var(--ball-silver) 0 70px, rgba(185,179,194,0.35) 110px, transparent 150px),
      radial-gradient(circle at 48% 42%, rgba(216,116,30,0.55) 0 40px, transparent 230px),
      radial-gradient(circle at 18% 70%, rgba(31,122,114,0.55), transparent 260px),
      radial-gradient(circle at 82% 55%, rgba(176,40,106,0.6), transparent 280px),
      radial-gradient(circle at 30% 20%, rgba(176,40,106,0.45), transparent 240px),
      radial-gradient(circle at 70% 15%, rgba(31,122,114,0.45), transparent 220px),
      linear-gradient(135deg, var(--label-purple), var(--label-dark) 55%, var(--label-purple));
  }
  .panel {
    position: absolute;
    background: var(--panel-bg);
    border: 2px solid var(--panel-edge);
    border-radius: 26px;
    color: var(--text-white);
    font-family: "Open Sans", sans-serif;
    text-align: center;
  }
  .panel__title {
    font-family: "Righteous", sans-serif;
    font-size: 34px; font-style: italic;
    margin-bottom: 10px;
  }
  .ingredients { left: 30px; top: 28px; width: 290px; height: 300px; padding: 18px 20px; }
  .ingredients .panel__title { color: var(--ingredient-green); text-align: left; }
  .ingredients p { font-size: 17px; line-height: 1.65; }
  .warning { left: 820px; top: 28px; width: 295px; height: 300px; padding: 18px 20px; }
  .warning .panel__title { color: var(--warning-red); }
  .warning p { font-size: 17px; line-height: 1.6; }
  .warning .warning__shake { font-weight: 700; font-size: 16px; margin-top: 10px; line-height: 1.3; }
  .flavors {
    left: 28px; top: 428px; width: 292px; height: 124px;
    display: flex; flex-direction: column; justify-content: center;
    font-family: "Righteous", sans-serif; font-size: 26px; line-height: 1.15;
    color: var(--flavor-yellow); letter-spacing: 1px;
  }
  .brand {
    position: absolute; left: 330px; top: 40px; width: 480px;
    text-align: center;
  }
  .brand__name {
    font-family: "Shrikhand", cursive;
    font-size: 118px; line-height: 0.95;
    color: var(--title-gold);
  }
  .brand__line { font-family: "Lobster", cursive; font-size: 56px; color: var(--text-white); margin-top: 18px; }
  .strength {
    position: absolute; left: 840px; top: 370px; width: 280px;
    text-align: center;
    font-family: "Open Sans", sans-serif; font-weight: 700;
    font-size: 34px; color: var(--text-white);
  }
  .batch {
    position: absolute; left: 893px; top: 430px; width: 225px; height: 90px;
    background: var(--batch-bg); color: var(--batch-text);
    border-radius: 6px;
    font-family: "Open Sans", sans-serif; font-weight: 600;
    font-size: 22px; line-height: 1.35;
    display: flex; flex-direction: column; justify-content: center; align-items: center;
  }
</style>
</head>
<body>
  <main class="label">
    <div class="label__art" role="img" aria-label="Disco-era artwork: dark purple background with colourful swirling rings, sunburst rays and a mirror disco ball at the bottom centre"></div>

    <section class="panel ingredients">
      <h2 class="panel__title">Ingredients:</h2>
      <p>USP, Kosher Vegetable Glycerin Propylene Glycol, Natural and artificial flavors May contain nicotine</p>
    </section>

    <div class="brand">
      <h1 class="brand__name">Velvet<br>Pulse</h1>
      <div class="brand__line">Glimmer</div>
    </div>

    <section class="panel warning">
      <h2 class="panel__title">WARNING:</h2>
      <p>Contents harmful do not swallow, avoid skin contact, keep out of children and pets.</p>
      <p class="warning__shake">SHAKE WELL<br>BEFORE USE</p>
    </section>

    <section class="panel flavors">
      <span>Lychee</span>
      <span>Passionfruit</span>
      <span>Tangerine</span>
    </section>

    <div class="strength">15ML-06MG</div>
    <div class="batch"><span>BN#0210</span><span>EXP 02/16</span></div>
  </main>
</body>
</html>
```